Plakat/Handzettel für Bildungs- und Gesundheitsservice
Zielgruppe
Wir benötigen eine Datei, die wir als
a.) Handzettel (DIN A4) sowie
b.) als Poster (DIN A1) ausdrucken können.
ACHTUNG:
a.) bitte in einem Format liefern, in dem den CODE XXXX immer 'selbst' austauschen können. Handzettel kann als Word-Datei.. das Poster lieber in einem Format, was mit Photoshop ggf. aufrufbar ist (weil wir den Code auf jedem Poster ändern müssen)
b.) Anliegend der Text der auf das Poster und Handzettel muss.
Aufgabenstellung
siehe Farben Website www.lindquel-akadem.com
bitte selbst entscheiden, ob Fotos auf dem Poster bzw. Handzettel sein sollen.

```html
<!DOCTYPE html>
<html lang="de">
<head>
<meta charset="utf-8">
<title>Lindquel Akadem – Plakat</title>
<link href="https://fonts.googleapis.com/css2?family=Anton&family=Montserrat:wght@400;500;600;700&display=swap" rel="stylesheet">
<style>
  :root{
    --blue:#3ab5d3;
    --green:#a5cd39;
    --navy:#1d4f6f;
    --ink:#3b3b3b;
    --white:#ffffff;
    --stage:#e9edef;
  }
  *{margin:0;padding:0;box-sizing:border-box}
  html,body{width:1200px;height:1177px;overflow:hidden;background:var(--stage)}
  .poster{position:absolute;left:197px;top:20px;width:806px;height:1137px;background:var(--white);overflow:hidden;font-family:"Montserrat",sans-serif}
  .top-bar{position:absolute;left:0;top:0;width:100%;height:10px;background:var(--green)}
  .photo{position:absolute}
  .photo-speaker{left:397px;top:10px;width:409px;height:500px;background:linear-gradient(180deg,#dfeef2 0%,#c7dde3 55%,#eef4f6 100%)}
  .photo-couple{left:440px;top:850px;width:366px;height:287px;background:linear-gradient(160deg,#b9c0c4 0%,#6f7f8c 60%,#3f4d5c 100%);border-top-left-radius:120px}
  .brand-name{position:absolute;left:0;width:486px;top:150px;text-align:center;font-weight:600;font-size:18px;letter-spacing:4px;color:#1b1b1b}
  .blob{position:absolute;left:0;top:0}
  .headline-line{position:absolute;left:66px;font-family:"Anton",sans-serif;font-weight:400;color:var(--white);line-height:1;text-transform:uppercase;white-space:nowrap}
  .headline-line.l1{top:219px;font-size:77px}
  .headline-line.l2{top:297px;font-size:106px}
  .tagline{position:absolute;left:68px;top:413px;font-family:"Anton",sans-serif;color:var(--white);font-size:25px;line-height:1.12;text-transform:uppercase;white-space:nowrap}
  .timeline{position:absolute;left:104px;top:560px;width:4px;height:370px;background:var(--green)}
  .hex{position:absolute;left:71px}
  .offer{position:absolute;left:163px}
  .offer h2{font-family:"Anton",sans-serif;font-weight:400;color:var(--navy);font-size:26px;line-height:1.1;text-transform:uppercase}
  .offer .note{font-size:11.5px;color:var(--navy);line-height:1.25;margin-top:3px}
  .offer ul{list-style:none;margin-top:6px}
  .offer li{position:relative;padding-left:30px;font-size:15px;font-weight:600;color:var(--ink);height:22.6px;line-height:22.6px}
  .offer li::before{content:"";position:absolute;left:0;top:6px;width:11px;height:11px;border-radius:50%;background:var(--blue)}
  .offer li::after{content:"";position:absolute;left:3px;top:8.5px;width:4px;height:2.5px;border-left:1.6px solid var(--white);border-bottom:1.6px solid var(--white);transform:rotate(-45deg)}
  .statement{position:absolute;left:68px;top:1014px;z-index:2;font-family:"Anton",sans-serif;color:var(--navy);font-size:12.4px;line-height:1.55;letter-spacing:-.1px;text-transform:uppercase;white-space:nowrap}
  .footer-bar{position:absolute;left:0;top:1072px;width:100%;height:65px;background:var(--blue)}
  .footer-url{position:absolute;left:68px;top:1087px;font-weight:700;font-size:17px;color:var(--white);letter-spacing:.5px}
  .access-box{position:absolute;left:458px;top:534px;width:299px;height:540px;background:var(--green);border-radius:14px 14px 0 0;color:var(--white);text-align:center}
  .access-box h3{margin-top:28px;font-family:"Anton",sans-serif;font-weight:400;font-size:26px;line-height:1.2;text-transform:uppercase}
  .access-box .code-intro{margin-top:6px;font-size:16px;font-weight:500;line-height:1.3}
  .code-pill{margin:12px auto 0;width:243px;height:31px;border-radius:16px;background:var(--blue);font-weight:700;font-size:16px;letter-spacing:9px;line-height:31px;padding-left:9px}
  .access-box .register{margin-top:12px;font-size:15.5px;font-weight:600;line-height:1.4}
  .access-box .register strong{font-weight:700;display:block}
</style>
</head>
<body>
<div class="poster">
  <div class="top-bar"></div>
  <div class="photo photo-speaker" role="img" aria-label="Foto: lächelnde Referentin mit Brille an einem Rednerpult in einem hellen Hörsaal"></div>

  <div class="brand-name">LINDQUEL AKADEM</div>

  <svg class="blob" width="806" height="620" viewBox="0 0 806 620">
    <path fill="#3ab5d3" d="M0,330 C0,240 60,186 160,186 L330,186 C420,186 486,262 486,340 C486,420 420,492 330,492 L160,492 C70,492 0,545 0,598 Z"/>
  </svg>

  <h1>
    <span class="headline-line l1">Lindquel</span>
    <span class="headline-line l2">Akadem</span>
  </h1>
  <p class="tagline">Hunderte von abendlichen<br>universitären Live-Veranstaltungen</p>

  <div class="timeline"></div>

  <svg class="hex" style="top:525px" width="67" height="76" viewBox="0 0 67 76">
    <polygon points="33.5,0 67,19 67,57 33.5,76 0,57 0,19" fill="#a5cd39"/>
    <g fill="none" stroke="#fff" stroke-width="1.6">
      <rect x="19" y="17" width="29" height="20" rx="1"/>
      <circle cx="33.5" cy="27" r="3"/>
      <circle cx="22" cy="46" r="3"/><circle cx="33.5" cy="46" r="3"/><circle cx="45" cy="46" r="3"/>
      <path d="M16,56 q6,-7 12,0 M27.5,56 q6,-7 12,0 M39,56 q6,-7 12,0"/>
    </g>
  </svg>
  <svg class="hex" style="top:766px" width="67" height="76" viewBox="0 0 67 76">
    <polygon points="33.5,0 67,19 67,57 33.5,76 0,57 0,19" fill="#a5cd39"/>
    <g fill="none" stroke="#fff" stroke-width="1.6">
      <rect x="14" y="26" width="38" height="24" rx="1"/>
      <path d="M33,50 v5 M25,56 h16"/>
      <path d="M21,38 v6 M33,38 v6 M45,38 v6 M14,38 h38"/>
      <circle cx="44" cy="22" r="7"/>
    </g>
  </svg>
  <svg class="hex" style="top:894px" width="67" height="76" viewBox="0 0 67 76">
    <polygon points="33.5,0 67,19 67,57 33.5,76 0,57 0,19" fill="#a5cd39"/>
    <g fill="none" stroke="#fff" stroke-width="1.6">
      <path d="M15,22 h26 v17 h-16 l-6,5 v-5 h-4 z"/>
      <path d="M41,30 h9 v16 h-3 v5 l-6,-5 h-12 v-7"/>
      <path d="M20,28 h16 M20,33 h12"/>
    </g>
  </svg>

  <section class="offer" style="top:532px">
    <h2>Live-Vorlesungen</h2>
    <p class="note">von 150 Professorinnen und Professoren<br>(mit Zertifikat der Teilnahme)</p>
    <ul>
      <li>Gesundheit</li>
      <li>Psychologie</li>
      <li>Medizin</li>
      <li>Marketing</li>
      <li>Führung</li>
      <li>und viele weitere Themen</li>
    </ul>
  </section>

  <section class="offer" style="top:762px">
    <h2>Live-praktische Seminare</h2>
    <ul>
      <li>Prävention von Burnout</li>
      <li>Resilienz Training</li>
      <li>Und viele weitere Themen</li>
    </ul>
  </section>

  <section class="offer" style="top:890px">
    <h2>Live-Dialogrunden</h2>
    <ul>
      <li>Beratung zu Erziehungsfragen</li>
      <li>Umgang mit Trauer</li>
      <li>Und viele weitere Themen</li>
    </ul>
  </section>

  <div class="footer-bar"></div>
  <div class="footer-url">WWW.LINDQUEL-AKADEM.COM</div>

  <aside class="access-box">
    <h3>Zugang zum virtuellen<br>Hörsaal auf dem<br>Lindquel Akadem</h3>
    <p class="code-intro">Ihr Code für eine<br>kostenfreie Nutzung:</p>
    <div class="code-pill">CODE XXXX</div>
    <p class="register">Melden Sie sich an:<strong>https://portal.lindquel-<br>akadem.com/register</strong></p>
  </aside>

  <div class="photo photo-couple" role="img" aria-label="Foto: Paar sitzt entspannt mit einem Laptop auf dem Sofa"></div>

  <p class="statement">Wir öffnen die Türen zum virtuellen Hörsaal für „alle“ Mitarbeitende,<br>denn bei uns ist wissenschaftliche Bildung für alle da.</p>
</div>
</body>
</html>
```